Motor Mate 4x6 Flyer

Need 4 x 6 Flyer with following language:

Willow Crest Motor Mate
Our Motor Mate Will Come to Your Home
Our Motor Mate will Drive Your Car to Nearest Gas Station
Our Motor Mate will Fill-up Your Car with Gas
Our Motor Mate will Immediately Return Your Car
Your Car Covered with $100k of Commercial Insurance
Member Dunmore Chamber of Commerce / Honest Merchant League
www.willowcrestmotormate.example

Place logos of Vortan, Brenn & Dorvane on Left Side of Flyer starting at top left corner, mid left side, left bottom corner.
Place logos of BoltNest, 12-Forty, Tesmira on opposite side right.....
Place Willow Crest Motor Mate Logo on both sides of very top that says Willow Crest Motor Mate

Target Market(s)

Upscale Home Owners

Font styles to use
Sans Serif

Colors
F0912C
F2A743
F7CA91
FBE8D2
FDF5EE

Requirements
Must have
• Flyer Must be Bright Orange

```html
<!DOCTYPE html>
<html lang="en">
<head>
<meta charset="utf-8">
<title>Willow Crest Motor Mate Flyer</title>
<link rel="stylesheet" href="https://fonts.googleapis.com/css2?family=Poppins:wght@400;500;600;700&family=Big+Shoulders+Stencil+Display:wght@700&display=swap">
<style>
  :root {
    --orange: #f15a22;
    --red: #e31e24;
    --ink: #0b0b0b;
    --paper: #ffffff;
    --arrow: #5e5e5e;
    --steel-light: #d9dadc;
    --steel-dark: #8a8c90;
    --pump: #f0912c;
  }
  * { margin: 0; padding: 0; box-sizing: border-box; }
  html, body {
    width: 796px; height: 1200px; overflow: hidden;
    background: var(--paper);
  }
  .flyer {
    position: relative; width: 796px; height: 1200px;
    background: var(--paper);
    font-family: "Poppins", sans-serif;
  }
  .flyer-art { position: absolute; inset: 0; }
  .brand-header {
    position: absolute; left: 78px; top: 38px;
    display: flex; align-items: center; gap: 36px;
  }
  .brand-mark {
    width: 100px; height: 100px; background: var(--red);
  }
  .brand-name {
    font-weight: 600; font-size: 74px; line-height: 1;
    color: var(--ink); letter-spacing: 1px;
  }
  .step {
    position: absolute; width: 240px; margin-left: -120px;
    text-align: center; color: var(--ink);
  }
  .step-number {
    font-family: "Big Shoulders Stencil Display", sans-serif;
    font-weight: 700; font-size: 108px; line-height: 84px;
    color: var(--orange);
  }
  .step-text { font-size: 18.5px; line-height: 23px; margin-top: 32px; }
  .step-text strong { font-weight: 600; display: block; }
  .partner {
    position: absolute; transform: translate(-50%, -50%);
    font-weight: 600; font-size: 21px; line-height: 1; white-space: nowrap;
  }
  .partner-vortan { color: var(--red); }
  .partner-brenn { color: var(--red); }
  .partner-dorvane { color: #1f5aa8; }
  .partner-tesmira { color: #1f5aa8; }
  .partner-twelve { color: #0b7a3e; }
  .partner-boltnest { color: var(--red); }
  .coverage {
    position: absolute; left: 0; right: 0; top: 998px;
    text-align: center; color: var(--paper);
  }
  .coverage-main { font-weight: 600; font-size: 36px; line-height: 44px; }
  .coverage-sub { font-weight: 600; font-size: 22px; line-height: 26px; }
  .membership {
    position: absolute; left: 0; right: 0; top: 1110px;
    text-align: center; font-size: 20.5px; color: var(--ink);
  }
  .membership .divider { color: var(--orange); padding: 0 4px; }
  .website {
    position: absolute; left: 0; right: 0; top: 1143px;
    text-align: center; font-size: 22px; font-weight: 600; color: var(--orange);
  }
</style>
</head>
<body>
<div class="flyer">
  <svg class="flyer-art" width="796" height="1200" viewBox="0 0 796 1200" aria-hidden="false">
    <defs>
      <clipPath id="upper-half"><rect x="0" y="0" width="796" height="627"/></clipPath>
      <marker id="arrow-head" viewBox="0 0 10 10" refX="5" refY="5" markerWidth="4" markerHeight="4" orient="auto">
        <path d="M0,0 L10,5 L0,10 Z" fill="var(--arrow)"/>
      </marker>
      <linearGradient id="pump-tone" x1="0" y1="0" x2="1" y2="1">
        <stop offset="0" stop-color="var(--steel-light)"/>
        <stop offset="0.55" stop-color="var(--pump)"/>
        <stop offset="1" stop-color="var(--steel-dark)"/>
      </linearGradient>
      <path id="title-arc" d="M71,472 A360,360 0 0 1 723,472"/>
    </defs>

    <rect class="orange-band" x="0" y="627" width="796" height="465" fill="var(--orange)"/>
    <circle class="black-ring" cx="397" cy="624" r="437" fill="var(--ink)" clip-path="url(#upper-half)"/>
    <circle class="step-disc" cx="397" cy="624" r="359" fill="var(--paper)"/>

    <text font-family="Poppins, sans-serif" font-weight="600" font-size="60" fill="var(--paper)">
      <textPath href="#title-arc" startOffset="50%" text-anchor="middle">Willow Crest Motor Mate</textPath>
    </text>

    <circle class="photo-frame" cx="397" cy="621" r="125" fill="var(--orange)"/>
    <circle class="photo-fill" cx="397" cy="621" r="113" fill="url(#pump-tone)" role="img" aria-label="Photo of an orange fuel nozzle filling a car's gas tank"/>

    <g class="cycle-arrows" fill="none" stroke="var(--arrow)" stroke-width="9" marker-end="url(#arrow-head)">
      <path d="M479.1,469.5 A175,175 0 0 1 568.2,587.6"/>
      <path d="M561.5,683.9 A175,175 0 0 1 462.6,786.3"/>
      <path d="M331.4,786.3 A175,175 0 0 1 232.5,683.9"/>
      <path d="M225.8,587.6 A175,175 0 0 1 314.9,469.5"/>
    </g>
  </svg>

  <header class="brand-header">
    <div class="brand-mark"></div>
    <div class="brand-name">MOTOR MATE</div>
  </header>

  <div class="step" style="left:397px; top:308px;">
    <div class="step-number">1</div>
    <div class="step-text">Our Motor Mate<strong>Will Come to<br>Your Home</strong></div>
  </div>
  <div class="step" style="left:642px; top:477px;">
    <div class="step-number">2</div>
    <div class="step-text" style="margin-top:25px;">Our Motor Mate<strong>Will Drive Your Car to<br>Nearest Gas Station</strong></div>
  </div>
  <div class="step" style="left:397px; top:761px;">
    <div class="step-number">3</div>
    <div class="step-text" style="margin-top:25px;">Our Motor Mate<strong>Will Fill-up Your<br>Car with Gas</strong></div>
  </div>
  <div class="step" style="left:165px; top:477px;">
    <div class="step-number">4</div>
    <div class="step-text" style="margin-top:25px;">Our Motor Mate<strong>Will Immediately<br>Return Your Car</strong></div>
  </div>

  <div class="partner partner-vortan" style="left:113px; top:695px;">Vortan</div>
  <div class="partner partner-brenn" style="left:150px; top:792px;">Brenn</div>
  <div class="partner partner-dorvane" style="left:240px; top:884px;">Dorvane</div>
  <div class="partner partner-tesmira" style="left:684px; top:703px;">Tesmira</div>
  <div class="partner partner-twelve" style="left:639px; top:792px;">12-Forty</div>
  <div class="partner partner-boltnest" style="left:561px; top:887px;">BoltNest</div>

  <div class="coverage">
    <div class="coverage-main">Your Car Covered with $100k</div>
    <div class="coverage-sub">of Commercial Insurance</div>
  </div>

  <div class="membership">Member <span class="divider">|</span> Dunmore Chamber of Commerce <span class="divider">|</span> Honest Merchant League</div>
  <div class="website">www.willowcrestmotormate.example</div>
</div>
</body>
</html>
```